Communication and Marketing agency needs a new presentation card

We are a group of communication and marketing agencies specialized in companies that are in the logistics and industrial sector. The head agency is VELUNEX Grupo and the group consists of 4 agencies: VELUNEX Media, VELUNEX Digital, VELUNEX Research and PlanoDeImagenes. We hace 4 offices in Spain (Madrid, Barcelona, Valencia and Murcia). We are looking for a clean and attractive design that transmits our experience, brand presence in the market and knowledge to those who receive the card.It has to maintain the colors of the logo that is attached.
logistics and industrial sector
Marketing department
Clean and attractive design

```html
<!DOCTYPE html>
<html lang="es">
<head>
<meta charset="utf-8">
<title>VELUNEX Grupo – Tarjeta de presentación</title>
<link rel="stylesheet" href="https://fonts.googleapis.com/css2?family=Open+Sans:wght@400;600;700&family=Roboto+Condensed:wght@700&display=swap">
<style>
  :root {
    --backdrop: #1f1f1f;
    --brand-red: #b21e2a;
    --paper: #ffffff;
    --graphite: #4f4d4b;
    --graphite-dark: #474543;
    --ink-grey: #4a4a4a;
    --on-red: #f6e3e4;
    --on-graphite: #efefef;
    --on-graphite-soft: #d9d9d9;
  }
  * { margin: 0; padding: 0; box-sizing: border-box; }
  html, body {
    width: 1125px; height: 1200px; overflow: hidden;
    background: var(--backdrop);
    font-family: "Open Sans", sans-serif;
  }
  .canvas { position: relative; width: 1125px; height: 1200px; }

  .card {
    position: absolute; left: 150px; width: 826px; height: 471px;
    box-shadow: 0 6px 22px rgba(0,0,0,.55);
  }
  .card--front { top: 98px; background: var(--paper); }
  .card--back { top: 631px; background: var(--graphite); }

  /* Front */
  .contact-panel {
    position: absolute; left: 0; top: 0; width: 350px; height: 100%;
    background: var(--brand-red); color: var(--on-red);
  }
  .edge-strip {
    position: absolute; right: 0; top: 0; width: 21px; height: 100%;
    background: var(--graphite-dark);
  }
  .person-name {
    position: absolute; left: 42px; top: 128px;
    font-size: 26px; font-weight: 700; color: #fff;
  }
  .person-role {
    position: absolute; left: 42px; top: 160px;
    font-size: 19px; font-weight: 400;
  }
  .contact-list { position: absolute; left: 42px; top: 207px; list-style: none; }
  .contact-list li {
    display: flex; align-items: center; height: 27px;
    font-size: 19px; font-weight: 400;
  }
  .contact-list svg { width: 18px; height: 18px; margin-right: 18px; fill: var(--on-red); }

  .brand-block {
    position: absolute; left: 350px; right: 21px; top: 168px;
    text-align: center;
  }
  .brand-name {
    font-size: 50px; font-weight: 600; color: var(--brand-red);
    letter-spacing: 2px; line-height: 1;
  }
  .brand-name .brand-sub { display: block; font-size: 30px; text-align: right; padding-right: 88px; margin-top: 4px; }
  .office-list {
    margin-top: 6px;
    font-family: "Roboto Condensed", sans-serif; font-weight: 700;
    font-size: 16px; color: var(--ink-grey); letter-spacing: .4px;
  }

  /* Back */
  .group-brand {
    position: absolute; left: 0; right: 0; top: 118px; text-align: center;
    font-size: 68px; font-weight: 600; color: var(--on-graphite);
    letter-spacing: 3px; line-height: 1;
  }
  .group-brand .brand-sub { display: block; font-size: 44px; text-align: right; padding-right: 240px; margin-top: 6px; }
  .agency-row {
    position: absolute; left: 30px; right: 30px; top: 344px;
    display: flex; justify-content: space-around; list-style: none;
  }
  .agency-row li {
    width: 180px; text-align: center;
    font-size: 21px; font-weight: 600; color: var(--on-graphite-soft);
    line-height: 1.05; letter-spacing: .5px;
  }
  .agency-row .brand-sub { display: block; font-size: 15px; text-align: right; padding-right: 16px; }
</style>
</head>
<body>
<main class="canvas">

  <section class="card card--front" aria-label="Anverso de la tarjeta">
    <div class="contact-panel">
      <h1 class="person-name">Selvana Ortuño</h1>
      <p class="person-role">Director</p>
      <ul class="contact-list">
        <li>
          <svg viewBox="0 0 20 20" aria-hidden="true"><path d="M3 7c0-2 3-4 7-4s7 2 7 4v1h-4V6.5H7V8H3z"/><path d="M5 9h10l2 8H3z"/><circle cx="10" cy="13" r="2" fill="#b21e2a"/></svg>
          910 472 618
        </li>
        <li>
          <svg viewBox="0 0 20 20" aria-hidden="true"><path d="M6 1h8a1 1 0 0 1 1 1v16a1 1 0 0 1-1 1H6a1 1 0 0 1-1-1V2a1 1 0 0 1 1-1zm1 3v11h6V4z"/></svg>
          631 908 254
        </li>
        <li>
          <svg viewBox="0 0 20 20" aria-hidden="true"><path d="M2 6l8 5 8-5v9H2z"/><path d="M2 4h16l-8 5z"/></svg>
          sortuno@velunex.es
        </li>
        <li>
          <svg viewBox="0 0 20 20" aria-hidden="true"><rect x="3" y="3" width="14" height="14" rx="2"/></svg>
          selvanaortuno
        </li>
        <li>
          <svg viewBox="0 0 20 20" aria-hidden="true"><circle cx="10" cy="10" r="8"/><path d="M2 10h16M10 2c3 3 3 13 0 16M10 2c-3 3-3 13 0 16" stroke="#b21e2a" stroke-width="1.2" fill="none"/></svg>
          velunex.es
        </li>
      </ul>
    </div>

    <div class="brand-block">
      <p class="brand-name">VELUNEX<span class="brand-sub">Media</span></p>
      <p class="office-list">MADRID/BARCELONA/VALENCIA/MURCIA</p>
    </div>
    <div class="edge-strip"></div>
  </section>

  <section class="card card--back" aria-label="Reverso de la tarjeta">
    <p class="group-brand">VELUNEX<span class="brand-sub">Grupo</span></p>
    <ul class="agency-row">
      <li>VELUNEX<span class="brand-sub">Digital</span></li>
      <li>VELUNEX<span class="brand-sub">Media</span></li>
      <li>VELUNEX<span class="brand-sub">Research</span></li>
      <li>PLANODE<br>IMAGENES</li>
    </ul>
  </section>

</main>
</body>
</html>
```